Business Card Design Project

Hi Designers, this project is currently on hold until the Logo is completed:
Please submit to the Logo project here:
http://jobs.pixelmarket.example/job.aspx?id=371905

Once logo is completed, it will be attached to this project for you to create business cards with show logo, company name and address

Maren T K Ashdown

Corwin's Meadow Pine Flock Co.
Hazelmere
Upper Brackwell
North Devon EX21 4TN

Tel: 01809 351846
Mobile: 07912 463078
email: maren@meadow-pine-flock.example
Updates

Project Deadline Extended
Reason: Sorry everyone, we have had a sick ewe and I am now behind with this one and need to extend the deadline. Best wishes Maren

The designer who wins the logo brief will be asked to design the business card. Many thanks Maren

Project Deadline Extended
Reason: Sorry everyone, just a chaotic time of year with animals. Need to extend the deadline again..... as I just haven't had enough time to take a good look.... Thank you for your understanding. Maren

Project Deadline Extended
Reason: Sorry everyone It is our busiest time of year with animals and just no time to spend going through such great designs. I will have to extend the deadline again and hopefully have some news very soon. Wishing you all a very happy Christmas and a happy and healthy new year. Maren & Corwin

Target Market(s)

High end market
Boutique restaurants for meat (it's not commercial lamb it's a slow matured quality meat more like venison/beef) expensive - specialized market

High End shoot clothing / wool / sheepskin rugs
Quality products

Industry/Entity Type

Business

Requirements
Must have
• based on the logo - (which Pixel Market has just been asked to do)
possibly based on a simplified picture of a Hebridean Ram (shows it's a Hebridean by it's horns as opposed to other black sheep!!)

```html
<!DOCTYPE html>
<html lang="en">
<head>
<meta charset="utf-8">
<title>Corwin's Meadow Pine Flock Co. — Business Cards</title>
<link href="https://fonts.googleapis.com/css2?family=Open+Sans:wght@400;600&display=swap" rel="stylesheet">
<style>
  :root {
    --backdrop: #d9d9d7;
    --ink: #2b2f2f;
    --paper: #efefec;
    --paper-text: #f2f2ef;
    --rule: #3a3e3e;
  }
  * { box-sizing: border-box; margin: 0; padding: 0; }
  html, body {
    width: 1200px; height: 676px; overflow: hidden;
    background: var(--backdrop);
    font-family: "Open Sans", Arial, sans-serif;
  }
  .canvas { position: relative; width: 1200px; height: 676px; }

  .card {
    position: absolute; top: 188px;
    width: 520px; height: 300px;
    overflow: hidden;
    box-shadow: 0 6px 18px rgba(0,0,0,0.25);
  }

  /* Card back */
  .card-back { left: 50px; background: var(--ink); }
  .card-back .brand {
    position: absolute; left: 0; right: 0; top: 96px;
    display: flex; flex-direction: column; align-items: center; gap: 18px;
  }
  .card-back .brand-dot {
    width: 64px; height: 64px; border-radius: 50%;
    border: 5px solid var(--paper-text);
  }
  .card-back .brand-name {
    color: var(--paper-text); font-size: 17px; font-weight: 400;
    letter-spacing: 0.04em;
  }

  /* Card front */
  .card-front { left: 630px; background: var(--paper); }
  .card-front .brand {
    position: absolute; left: 26px; top: 26px;
    display: flex; align-items: center; gap: 12px;
  }
  .card-front .brand-dot {
    width: 30px; height: 30px; border-radius: 50%;
    border: 3px solid var(--ink);
  }
  .card-front .brand-name {
    color: var(--ink); font-size: 13px; font-weight: 400; letter-spacing: 0.03em;
  }
  .holder {
    position: absolute; right: 28px; top: 84px;
    color: var(--ink); font-size: 17px; font-weight: 600;
  }
  .holder-rule {
    position: absolute; left: 300px; right: 0; top: 112px;
    height: 1px; background: var(--rule);
  }
  .band {
    position: absolute; left: 0; right: 0; top: 126px; height: 86px;
    background: var(--ink);
  }
  .address {
    position: absolute; left: 34px; top: 134px;
    color: var(--paper-text); font-size: 11px; line-height: 17px;
    font-style: normal;
  }
  .contact {
    position: absolute; left: 34px; top: 218px;
    color: var(--ink); font-size: 11px; line-height: 17px;
  }
  .seal {
    position: absolute; left: 352px; top: 112px; width: 140px; height: 140px;
  }
</style>
</head>
<body>
<main class="canvas">

  <section class="card card-back" aria-label="Business card back">
    <div class="brand">
      <span class="brand-dot"></span>
      <span class="brand-name">Corwin's Meadow Pine Flock Co.</span>
    </div>
  </section>

  <section class="card card-front" aria-label="Business card front">
    <div class="brand">
      <span class="brand-dot"></span>
      <span class="brand-name">Corwin's Meadow Pine Flock Co.</span>
    </div>

    <p class="holder">Maren T K Ashdown</p>
    <div class="holder-rule"></div>

    <div class="band"></div>
    <address class="address">
      Corwin's Meadow Pine Flock Co.<br>
      Hazelmere<br>
      Upper Brackwell<br>
      North Devon EX21 4TN
    </address>

    <p class="contact">
      Tel: 01809 351846<br>
      Mobile: 07912 463078<br>
      email: maren@meadow-pine-flock.example
    </p>

    <svg class="seal" viewBox="0 0 140 140" aria-hidden="true">
      <circle cx="70" cy="70" r="62" fill="var(--paper)" stroke="var(--ink)" stroke-width="8"/>
    </svg>
  </section>

</main>
</body>
</html>
```